Women's Shelter Website Design

We are working with a Women's Shelter in California. They provide services and shelter for women and mothers throughout California.
Some sites to use for inspiration:
https://harborlightrefuge.org
https://kpelm.org
https://www.brtoqe.org
https://gdmfelbrook.org
https://www.vmshelterly.org (I love the banner, navigation and upper navigation)
https://birchmoorrefuge.org (love the idea of an EXIT NOW button)
Thank you for taking the time to consider designing a website for us. We are web developers based in Stockton, CA, USA. Most of our projects go through the same process. Understanding this process may help you win a project with us. We custom-code all of our websites in-house. We don’t have any requirements as to what tools you use for your design, but we ask that you follow these guidelines.
IMAGES:
If you use any images or icons in the design, we ask that you have a link to the asset so we can purchase the image/icon. Most of the designs we submit do not have the customer’s images on them unless they have some great images. Be creative; show us the feeling you are trying to portray with your image choices. Use any royalty-free site you choose. We subscribe to Adobe and mainly use their images, but we can purchase images outside of Adobe. PLEASE NOTE: we will not submit designs to clients with watermarks on the images.
FONTS:
We ask that you identify the fonts you’re using in the design. This can be done in a message if you want. We typically use Google Fonts and Adobe Fonts.
CONTENT:
We're always open to different content and ideas. We often submit designs with stock images so the client can see our vision. We typically take pictures after the website launch to use their images with our vision. Lorem Ipsum is fine for paragraphs, but we ask that you make the Headers with correct English. We want to be able to show the vision and identify the sections of the website.
INSPIRATION:
We typically add a couple of links in the brief of websites we like to help you get started in your design.
REVISIONS:
We do not often ask for revisions of the designs unless we see something in the design that may not appeal to the client. If there are slight changes that we want to make, we do that in the development process.
FEEDBACK:
We rarely give feedback on designs during the design process. We are working on many website projects and do not have the time to provide feedback. We usually respond if your request is well thought out and asks specific questions, but a note asking “feedback, please” usually goes unanswered.

```html
<!DOCTYPE html>
<html lang="en">
<head>
<meta charset="utf-8">
<title>Wingrise Women's Shelter</title>
<link href="https://fonts.googleapis.com/css2?family=Poppins:wght@400;500;600;700;800;900&display=swap" rel="stylesheet">
<style>
:root{
  --purple:#4a1f8c;
  --purple-deep:#3a1676;
  --coral:#f0695a;
  --green:#3db54a;
  --dark:#262626;
  --ink:#222;
  --muted:#444;
  --light:#f2f2f2;
  --footer:#2f2f2f;
}
*{margin:0;padding:0;box-sizing:border-box}
html,body{width:1200px;height:3949px;overflow:hidden}
body{font-family:'Poppins',sans-serif;color:var(--ink);background:#fff;position:relative}
.abs{position:absolute}
a{color:inherit;text-decoration:none}

/* top bar */
.topbar{left:0;top:0;width:1200px;height:61px;background:#efefef}
.social{display:flex;gap:18px;align-items:center}
.social span{width:22px;height:22px;border-radius:50%;background:#555;display:block}
.topbar .social{left:72px;top:19px}
.cta{top:0;height:61px;display:flex;align-items:center;justify-content:center;color:#fff;font-weight:600;font-size:16px;border-radius:31px 0 0 31px;letter-spacing:.3px}
.cta-help{left:723px;width:180px;background:var(--purple)}
.cta-vol{left:886px;width:170px;background:var(--coral)}
.cta-don{left:1034px;width:166px;background:var(--green)}

/* header */
.brand{display:flex;align-items:center;gap:10px}
.brand-dot{width:40px;height:40px;border-radius:50%;background:linear-gradient(160deg,var(--coral),var(--purple))}
.brand-name{font-weight:700;font-size:34px;color:var(--purple-deep);letter-spacing:-1px}
.header .brand{left:74px;top:106px}
.nav{left:344px;top:120px;display:flex;gap:30px;font-size:14px;font-weight:600;color:#333;letter-spacing:.3px}

/* hero */
.hero{left:0;top:195px;width:1200px;height:665px;background:linear-gradient(90deg,#5a2aa6 0%,#6a3aa8 35%,#8a7a8a 55%,#a99683 75%,#6f5b4f 100%)}
.hero-title{left:72px;top:170px;font-weight:900;font-size:86px;line-height:74px;color:#fff}
.hero-title .accent{color:var(--coral)}
.btn{display:flex;align-items:center;justify-content:center;border-radius:28px;font-weight:700;font-size:18px;color:#fff}
.hero .btn-outline{left:74px;top:432px;width:180px;height:55px;border:2px solid #fff}
.hero .btn-green{left:262px;top:432px;width:178px;height:55px;background:var(--green)}

.mark{width:22px;height:22px;border-radius:50%;background:linear-gradient(160deg,var(--coral),var(--purple))}
.sec-title{font-weight:700;font-size:38px;color:var(--ink)}

/* what we do */
.what-title{left:0;top:930px;width:1200px;text-align:center}
.what-title .mark{display:inline-block;vertical-align:top;margin-right:6px}
.what-lead{left:140px;top:995px;width:920px;text-align:center;font-size:29px;line-height:43px;color:#333}
.card{top:1132px;width:241px;height:336px;border-radius:28px;background:linear-gradient(160deg,#e85a5a 0%,#b23a6c 50%,#4a1c8c 100%);color:#fff;text-align:center;padding:26px 18px 0}
.card svg{display:block;margin:0 auto 14px}
.card h3{font-size:21px;font-weight:700;line-height:30px}
.card p{margin-top:12px;font-size:15px;line-height:26px}

/* welcome */
.welcome{left:0;top:1578px;width:1200px;height:633px;background:var(--dark)}
.welcome-photo{left:600px;top:0;width:600px;height:633px;background:linear-gradient(120deg,#6b4e36,#8a7460 45%,#3a3a44)}
.welcome h2{left:74px;top:100px;color:#fff;font-weight:700;font-size:40px;line-height:47px}
.welcome .mark{left:46px;top:80px}
.welcome p{left:74px;top:210px;width:520px;color:#eee;font-size:17px;line-height:35px}
.welcome .btn{left:74px;top:501px;width:180px;height:54px;background:var(--green)}

/* stats */
.stats-title{left:0;top:2280px;width:1200px;text-align:center;font-size:40px;font-weight:700}
.stat{top:2360px;width:340px;text-align:center}
.stat b{display:block;font-size:66px;font-weight:700;line-height:78px;background:linear-gradient(90deg,#e85a5a,var(--purple));-webkit-background-clip:text;background-clip:text;color:transparent}
.stat span{display:block;margin-top:12px;font-size:18px;line-height:28px;color:#444}

/* story */
.story{left:0;top:2588px;width:1200px;height:583px;background:var(--light)}
.story-photo{left:500px;top:0;width:700px;height:583px;background:linear-gradient(90deg,var(--light) 0%,#c9c3c0 25%,#a7a09c 60%,#8f8a88 100%)}
.story .mark{left:74px;top:110px}
.story h2{left:100px;top:128px;font-size:40px;font-weight:700;line-height:42px;color:var(--ink)}
.story h2 .accent{color:var(--purple)}
.story p{left:74px;top:250px;width:520px;font-size:17px;line-height:35px;color:#333}
.story .btn{left:76px;top:424px;width:243px;height:55px;background:var(--green)}

/* subscribe */
.sub-title{left:0;top:3245px;width:1200px;text-align:center}
.sub-title .mark{display:inline-block;vertical-align:top;margin-right:4px}
.sub-text{left:110px;top:3322px;width:980px;text-align:center;font-size:18px;line-height:35px;color:#333}
.field{top:3427px;height:56px;border:2px solid #d8d8d8;border-radius:28px;padding-left:22px;display:flex;align-items:center;font-size:14px;color:#555}
.sub-btn{left:778px;top:3427px;width:331px;height:56px;background:linear-gradient(90deg,#e85a5a,var(--purple));font-size:19px}

/* footer */
.footer{left:0;top:3583px;width:1200px;height:302px;background:var(--footer);color:#fff}
.footer .brand{left:74px;top:110px}
.footer .brand-name{color:#fff;font-size:40px}
.fcol{top:65px}
.fcol h4{font-size:22px;font-weight:600;margin-bottom:12px}
.fcol li{list-style:none;font-size:15px;line-height:35px;color:#ddd}
.fcol p{font-size:15px;line-height:27px;color:#ddd;margin-bottom:8px}
.footer .social{margin-top:14px}
.footer .social span{background:#ddd}
.exit{left:12px;top:3826px;width:123px;height:41px;border-radius:21px;background:var(--coral);color:#fff;font-size:13px;font-weight:700;display:flex;align-items:center;justify-content:center}
.copy{left:0;top:3885px;width:1200px;height:64px;background:var(--footer);border-top:1px solid #444;color:#ddd;font-size:14px;display:flex;align-items:center;justify-content:center}
</style>
</head>
<body>

<div class="abs topbar">
  <div class="abs social" aria-label="Social links"><span></span><span></span><span></span><span></span><span></span></div>
</div>
<a class="abs cta cta-help">GET HELP NOW</a>
<a class="abs cta cta-vol">VOLUNTEER</a>
<a class="abs cta cta-don">DONATE</a>

<header class="header">
  <div class="abs brand"><span class="brand-dot"></span><span class="brand-name">Wingrise</span></div>
  <nav class="abs nav"><a>HOME</a><a>ABOUT</a><a>SERVICES</a><a>COMMUNITY</a><a>STORIES</a><a>GET INVOLVED</a><a>SUPPORT</a><a>CONTACT US</a></nav>
</header>

<section class="abs hero" role="img" aria-label="Photo of a smiling older woman holding a bowl at a community meal, purple overlay on the left">
  <h1 class="abs hero-title">Wingrise<br><span class="accent">...Women's<br>Shelter..</span></h1>
  <a class="abs btn btn-outline">Read More</a>
  <a class="abs btn btn-green">Donate Now</a>
</section>

<h2 class="abs sec-title what-title"><span class="mark"></span>What We Do</h2>
<p class="abs what-lead">Excepteur sint occaecat cupidatat non proident sunt in culpa qui officia deserunt mollit.</p>

<div class="abs card" style="left:75px">
  <svg width="90" height="86" viewBox="0 0 90 86" fill="none" stroke="#7fe08a" stroke-width="3"><path d="M8 40 45 8l37 32"/><path d="M18 32v46h54V32"/><circle cx="45" cy="48" r="8"/><path d="M32 78c0-10 6-16 13-16s13 6 13 16"/></svg>
  <h3>Emergency<br>Shelters</h3>
  <p>Nemo enim ipsam voluptatem quia voluptas sit aspernatur aut odit aut fugitsed.</p>
</div>
<div class="abs card" style="left:345px">
  <svg width="90" height="86" viewBox="0 0 90 86" fill="none" stroke="#7fe08a" stroke-width="3"><path d="M6 38 45 8l39 30"/><path d="M16 30v48h58V30"/><rect x="38" y="52" width="14" height="26"/><rect x="22" y="44" width="10" height="10"/><rect x="58" y="44" width="10" height="10"/><circle cx="45" cy="32" r="6"/></svg>
  <h3>Residential<br>Program</h3>
  <p>Nemo enim ipsam voluptatem quia voluptas sit aspernatur aut odit aut fugitsed.</p>
</div>
<div class="abs card" style="left:615px">
  <svg width="90" height="86" viewBox="0 0 90 86" fill="none" stroke="#7fe08a" stroke-width="3"><circle cx="45" cy="28" r="16"/><path d="M16 80c0-18 12-28 29-28s29 10 29 28z"/></svg>
  <h3>Womens's<br>Resource Center</h3>
  <p>Nemo enim ipsam voluptatem quia voluptas sit aspernatur aut odit aut fugitsed.</p>
</div>
<div class="abs card" style="left:885px">
  <svg width="90" height="86" viewBox="0 0 90 86" fill="none" stroke="#7fe08a" stroke-width="3"><circle cx="45" cy="43" r="10"/><circle cx="15" cy="15" r="8"/><circle cx="75" cy="15" r="8"/><circle cx="15" cy="71" r="8"/><circle cx="75" cy="71" r="8"/><path d="M22 22l15 13M68 22 53 35M22 64l15-13M68 64 53 51"/></svg>
  <h3>Community<br>Outreach</h3>
  <p>Nemo enim ipsam voluptatem quia voluptas sit aspernatur aut odit aut fugitsed.</p>
</div>

<section class="abs welcome">
  <div class="abs welcome-photo" role="img" aria-label="Portrait of a woman sitting in a warmly lit room"></div>
  <svg class="abs" style="left:540px;top:0" width="130" height="633" viewBox="0 0 130 633" aria-hidden="true"><path d="M0 0H130C110 90 60 140 80 240 96 320 50 360 80 440 60 520 10 570 0 633H0Z" fill="#262626"/></svg>
  <span class="abs mark"></span>
  <h2 class="abs">Welcome to<br>Wingrise Women's Shelter</h2>
  <p class="abs">Nemo enim ipsam voluptatem quia voluptas sit aspernatur aut odit aut fugit, sed quia consequuntur magni dolores eos qui ratione voluptatem sequi nesciunt. Neque porro quisquam est, qui dolorem ipsum quia dolor sit amet, consectetur, adipisci velit, sed quia non numquam eius modi tempora incidunt ut labore et dolore magnam aliquam quaerat voluptatem.</p>
  <a class="abs btn">Read More</a>
</section>

<h2 class="abs stats-title">Lives Changed Thanks to People Just Like You!</h2>
<div class="abs stat" style="left:69px"><b>235,215</b><span>Excepteur sint occaecat<br>cupidatat</span></div>
<div class="abs stat" style="left:430px"><b>5,215</b><span>Excepteur sint occaecat<br>cupidatat</span></div>
<div class="abs stat" style="left:792px"><b>135,260</b><span>Excepteur sint occaecat<br>cupidatat</span></div>

<section class="abs story">
  <div class="abs story-photo" role="img" aria-label="Photo of a thoughtful woman sitting on a staircase"></div>
  <span class="abs mark"></span>
  <h2 class="abs">Meet Elena<br><span class="accent">.....Watch Her Story</span></h2>
  <p class="abs">“ Nemo enim ipsam voluptatem quia voluptas sit aspernatur aut odit aut fugit, sed quia consequuntur magni dolores eos qui ratione voluptatem sequi nesciunt. Neque porro quisquam est..”</p>
  <a class="abs btn">Watch Full Story</a>
</section>

<h2 class="abs sec-title sub-title"><span class="mark"></span>Stay Connected</h2>
<p class="abs sub-text">“ Nemo enim ipsam voluptatem quia voluptas sit&nbsp; aspernatur aut odit aut fugit, sed quia consequuntur magni dolores eos qui ratione voluptatem sequi nesciunt.</p>
<div class="abs field" style="left:93px;width:331px">Enter Name</div>
<div class="abs field" style="left:437px;width:329px">Enter Email Address</div>
<a class="abs btn sub-btn">Subscribe Now</a>

<footer class="abs footer">
  <div class="abs brand"><span class="brand-dot"></span><span class="brand-name">Wingrise</span></div>
  <div class="abs fcol" style="left:351px"><h4>Quick Links</h4><ul><li>Duis aute irure</li><li>Dolor in reprehen</li><li>Derit in voluptate</li><li>Velit esse</li><li>Excepteur sint occaecat</li></ul></div>
  <div class="abs fcol" style="left:643px"><h4>Resources</h4><ul><li>Duis aute irure</li><li>Dolor in reprehen</li><li>Derit in voluptate</li><li>Velit esse</li></ul></div>
  <div class="abs fcol" style="left:882px;width:300px"><h4>Get in Touch</h4>
    <p>418 Alder Cove Suite 212,<br>Stockton 95202, United States</p>
    <p>+1-555-014-2290</p>
    <p>hello@wingriseshelter.org</p>
    <div class="social"><span></span><span></span><span></span><span></span><span></span></div>
  </div>
</footer>
<a class="abs exit">✕ EXIT NOW</a>
<div class="abs copy">Copyright © 2023 Company Name All Rights Reserved.</div>

</body>
</html>
```